Nutrition-Cooking Website

Hello!
I am in a need of a lovely looking website for my new nutrition practice. I am looking for something sleek, sophisticated, professional yet also welcoming.

Here is a current layout which can be tweaked or overhauled. I feel like the website is not quite what I want so thats why I need your help!!
http://tolvanfolio.example/RENATA-OSSLER-concept-15/

Two websites I like are: (layout similar to www.marquetta.example) or http://www.pernillavostraken.example

Here are the tabs for the website:
About Registered Dietitian Healthy Recipes Philanthropy Shop Features Contact Blog

Features for the Home page include:
Slideshow with 3 rotating updates (like www.marquetta.example)
Video Box (like www.marquetta.example)
Recent Recipes (like http://harrowfield7731.example)
Recent Posts (like http://harrowfield7731.example)
Food Knowledge Box- quick tidbits on laws on food (like www.marquetta.example- she has food wisdom)
Tried and True Benefits of Mediterranean Cuisine (like www.marquetta.example)
Picture of me with brief quote/bio (like www.bettinoruval.example)
Social media buttons

Color Scheme:
• I like the white with gold embroidery or the pretty bluish/purplish in the first pic would be awesome with the slight pink undertones (http://glossedtwirl.example/2012/10/quorvel-marigelle-collection-by-tansley/)
• Also like this goldish background- exotic/sophisticated- http://www.thewhirlingcook.example/Home.html
• Also like the rustic goldish look in the background like this-
ohttp://img.prentlo.example/vexomarks_rsvp_vintage_rustic_gold_swirls_invitation-p161658028764768924bebn6_400.jpg
o http://img.prentlo.example/vexomarks_ornamental_rustic_gold_swirls_invitation-p161776340110432961bvddb_400.jpg
• maybe can have the vines as grapes/olives
OPEN TO ALL DIFFERENT COLORS SCHEMES- whatever looks, clean, sophisticated and professional

Logo:
• Attached is the logo

Budget is flexible. If you think you can improve the website- please do so :)

Target Market(s)

health conscious individuals of all ages

Industry/Entity Type

Embroidery

Requirements
Must have
• clean and sharp look
professional looking
Should not have
• too much busyness

```html
<!DOCTYPE html>
<html lang="en">
<head>
<meta charset="utf-8">
<title>Renata Ossler RD</title>
<link rel="stylesheet" href="https://fonts.googleapis.com/css2?family=Cinzel:wght@400;700&family=PT+Sans:wght@400;700&display=swap">
<style>
  :root {
    --ink: #2f2a27;
    --text: #5a5552;
    --muted: #8a8582;
    --rose: #c0607f;
    --rose-text: #b5577a;
    --sky: #8fb1cb;
    --panel: #e7e1db;
    --page: #f7f6f4;
    --card: #f0eeeb;
    --line: #dedad6;
    --video: #333130;
    --white: #ffffff;
  }
  * { box-sizing: border-box; margin: 0; padding: 0; }
  html, body { width: 1200px; height: 896px; overflow: hidden; }
  body {
    position: relative;
    background: var(--page);
    font-family: "PT Sans", Arial, sans-serif;
    color: var(--text);
    font-size: 12px;
  }
  a { color: var(--rose-text); text-decoration: none; }

  /* Header */
  .site-header { position: absolute; left: 0; top: 0; width: 1200px; height: 122px; background: var(--white); }
  .brand { position: absolute; left: 196px; top: 26px; font-family: "Cinzel", serif; font-size: 21px; letter-spacing: 1px; color: var(--ink); display: flex; align-items: center; gap: 8px; }
  .brand-mark { width: 8px; height: 8px; border-radius: 50%; background: #c9b48f; }
  .utility { position: absolute; left: 770px; top: 16px; display: flex; gap: 8px; font-size: 10px; color: var(--muted); }
  .utility .sep { color: #ccc; }
  .cart { position: absolute; left: 917px; top: 14px; display: flex; align-items: center; gap: 8px; font-size: 10px; color: var(--muted); }
  .search { position: absolute; left: 797px; top: 42px; width: 214px; height: 23px; border: 1px solid #cfcfcf; font-size: 10px; color: #b8b8b8; padding: 5px 8px; }
  .search svg { position: absolute; right: 4px; top: 3px; }
  .dotted { position: absolute; left: 196px; top: 80px; width: 815px; border-top: 1px dotted #cfcac4; }
  .main-nav { position: absolute; left: 196px; top: 87px; display: flex; font-family: "Cinzel", serif; font-size: 12px; color: var(--ink); }
  .main-nav span { display: block; height: 26px; line-height: 27px; padding: 0 4px; }
  .main-nav .current { border-bottom: 2px solid #d9cdbf; }
  .main-nav .shop { background: var(--rose); color: var(--white); padding: 0 10px; }

  /* Hero */
  .hero-band { position: absolute; left: 0; top: 122px; width: 1200px; height: 345px;
    background: repeating-linear-gradient(45deg, #ebe7e2 0 2px, #efebe7 2px 4px); }
  .hero-photo { position: absolute; left: 196px; top: 122px; width: 507px; height: 291px;
    background: radial-gradient(ellipse at 40% 45%, #d08a45 0%, #b46a35 30%, #6f6a3a 55%, #e9e4dc 80%); }
  .hero-notch { position: absolute; left: 252px; top: 401px; }
  .hero-caption { position: absolute; left: 198px; top: 436px; font-family: "Cinzel", serif; font-size: 11px; color: var(--ink); white-space: nowrap; }
  .hero-caption a { margin-left: 6px; }
  .dots { position: absolute; left: 625px; top: 438px; display: flex; gap: 7px; }
  .dots i { width: 10px; height: 10px; border-radius: 50%; background: #b7aea4; display: block; }
  .dots i:first-child { background: #3a3532; }
  .welcome { position: absolute; left: 703px; top: 122px; width: 308px; height: 345px; background: var(--panel); padding: 33px 34px; }
  .welcome h1 { font-family: "Cinzel", serif; font-weight: 400; font-size: 17px; line-height: 20px; color: var(--ink); letter-spacing: .5px; }
  .welcome p { margin-top: 12px; font-size: 11.5px; line-height: 14.5px; color: var(--text); }
  .cta { position: absolute; left: 34px; width: 240px; height: 46px; color: var(--white); padding: 7px 15px; }
  .cta b { display: block; font-family: "Cinzel", serif; font-weight: 400; font-size: 17px; letter-spacing: 1px; line-height: 18px; }
  .cta small { display: block; font-size: 9px; letter-spacing: 2px; opacity: .85; }
  .cta svg { position: absolute; right: 14px; top: 16px; }
  .cta-register { top: 209px; background: var(--rose); }
  .cta-browse { top: 266px; background: var(--sky); }

  /* Intro cards */
  .intro { position: absolute; left: 196px; top: 475px; width: 507px; height: 110px; background: var(--card); }
  .intro-item { position: absolute; top: 18px; width: 232px; }
  .intro-item h2, .section-title { font-family: "Cinzel", serif; font-weight: 400; font-size: 13px; color: var(--ink); letter-spacing: .5px; }
  .intro-item p { margin-top: 4px; font-size: 12px; line-height: 14.5px; white-space: nowrap; }
  .intro-item a { display: block; margin-top: 6px; }

  /* Lists */
  .section-title { position: absolute; white-space: nowrap; }
  .pager { position: absolute; display: flex; }
  .pager span { width: 25px; height: 16px; background: #ebe8e4; display: flex; align-items: center; justify-content: center; }
  .pager span + span { background: #dcd8d3; }
  .col-rule { position: absolute; border-top: 1px solid var(--line); }
  .posts { position: absolute; left: 196px; top: 638px; width: 160px; border-right: 1px solid var(--line); height: 258px; }
  .post { position: absolute; left: 1px; width: 154px; font-size: 11.5px; line-height: 14.5px; white-space: nowrap; }
  .post .thumb { float: left; width: 51px; height: 39px; margin: 2px 8px 2px 0; background: linear-gradient(135deg, #5a3a35, #efe8e4 60%, #8a5a4a); }
  .post b { color: var(--ink); font-size: 11px; }
  .recipe { position: absolute; width: 148px; font-size: 12px; line-height: 14.5px; }
  .recipe .photo { width: 148px; height: 109px; margin-bottom: 9px; }
  .recipe a { display: block; margin-top: 5px; }

  /* Sidebar */
  .video { position: absolute; left: 720px; top: 524px; width: 277px; height: 134px; background: radial-gradient(ellipse at center, #4a4745, var(--video)); }
  .video svg { position: absolute; left: 131px; top: 58px; }
  .video-text { position: absolute; left: 719px; top: 675px; width: 290px; font-size: 12px; line-height: 14.5px; white-space: nowrap; letter-spacing: -0.25px; }
  .video-text small { display: block; margin-top: 4px; font-size: 10px; letter-spacing: -0.3px; color: var(--muted); }
  .side-rule { position: absolute; left: 703px; top: 745px; width: 308px; border-top: 1px solid var(--line); }
  .tweets-title { position: absolute; left: 721px; top: 768px; display: flex; align-items: center; gap: 10px; }
  .tweets-title i { width: 13px; height: 13px; border-radius: 50%; background: #c7c3bf; display: block; }
  .tweets-title span { font-family: "Cinzel", serif; font-size: 13px; color: var(--ink); }
  .tweet { position: absolute; left: 722px; top: 804px; width: 275px; font-size: 12px; line-height: 14.5px; white-space: nowrap; }
  .tweet-rule { position: absolute; left: 722px; top: 877px; width: 270px; border-top: 1px dotted #cfcac4; }
  .tweet-next { position: absolute; left: 722px; top: 888px; font-size: 12px; white-space: nowrap; }
</style>
</head>
<body>
  <header class="site-header">
    <div class="brand"><span>Renata Ossler RD</span><span class="brand-mark"></span></div>
    <div class="utility"><span>Login</span><span class="sep">|</span><span>Sitemap</span><span class="sep">|</span><span>Help</span></div>
    <div class="cart">
      <svg width="17" height="15" viewBox="0 0 17 15"><path d="M0 1h3l2 9h9l2-7H4" fill="none" stroke="#b9b9b9" stroke-width="2"/><circle cx="6" cy="13" r="1.5" fill="#b9b9b9"/><circle cx="13" cy="13" r="1.5" fill="#b9b9b9"/></svg>
      <span>Shopping Chart</span>
    </div>
    <div class="search">Search
      <svg width="16" height="16" viewBox="0 0 16 16"><circle cx="6.5" cy="6.5" r="4.5" fill="none" stroke="#888" stroke-width="2"/><path d="M10 10l4 4" stroke="#888" stroke-width="2.5"/></svg>
    </div>
    <div class="dotted"></div>
    <nav class="main-nav">
      <span class="current">Home</span>
      <span style="margin-left:14px">About</span>
      <span style="margin-left:15px">Registered Dietitian</span>
      <span style="margin-left:19px">Healthy Recipes</span>
      <span style="margin-left:16px">Philantrophy</span>
      <span class="shop" style="margin-left:21px">Shop</span>
      <span style="margin-left:14px">Features</span>
      <span style="margin-left:16px">Contact</span>
      <span style="margin-left:20px">Blog</span>
    </nav>
  </header>

  <section class="hero-band"></section>
  <div class="hero-photo" role="img" aria-label="Photo of a toasted sandwich roll with grilled patty and lettuce on a plate"></div>
  <svg class="hero-notch" width="22" height="12" viewBox="0 0 22 12"><path d="M0 12L11 0l11 12z" fill="#ede9e5"/></svg>
  <p class="hero-caption">Pellentesque lorem ligula, rhoncus at malesuada in. <a>Read more</a></p>
  <div class="dots"><i></i><i></i><i></i></div>

  <aside class="welcome">
    <h1>Welcome to Renata<br>Ossler RD</h1>
    <svg style="position:absolute;left:145px;top:64px" width="130" height="6"><rect width="130" height="6" fill="#ddd7d0"/></svg>
    <p>Fusce in ornare erat. Nam lacinia tincidunt dapibus. Duis sed iaculis neque. Aenean sit amet urna eros, vitae semper arcu. Aliquam dignissim ipsum id sapien auctor ac semper diam fermentum. Maecenas pretium magna nec turpis porttitor quis sagittis enim malesuada. Nulla id lectus augue,</p>
    <a class="cta cta-register"><b>Register</b><small>For a cooking class</small>
      <svg width="9" height="14" viewBox="0 0 9 14"><path d="M1 1l6 6-6 6" fill="none" stroke="#fff" stroke-width="1.6"/></svg></a>
    <a class="cta cta-browse"><b>Browse Recipes</b><small>For healthy dietitian</small>
      <svg width="9" height="14" viewBox="0 0 9 14"><path d="M1 1l6 6-6 6" fill="none" stroke="#fff" stroke-width="1.6"/></svg></a>
  </aside>

  <section class="intro">
    <div class="intro-item" style="left:14px">
      <h2>Food Philosophy</h2>
      <p>Growing up on Mediteranian cuisine, my<br>food philosophy was influenced to be based.</p>
      <a>Read more</a>
    </div>
    <div class="intro-item" style="left:268px">
      <h2>Food Knowledge</h2>
      <p>Growing up on Mediteranian cuisine, my<br>food philosophy was influenced to be based.</p>
      <a>Read more</a>
    </div>
  </section>

  <h2 class="section-title" style="left:196px;top:610px">Recent Posts</h2>
  <h2 class="section-title" style="left:364px;top:610px">Recent Recipes</h2>
  <div class="pager" style="left:630px;top:609px"><span><svg width="5" height="8"><path d="M5 0v8L0 4z" fill="#bbb"/></svg></span><span><svg width="5" height="8"><path d="M0 0v8l5-4z" fill="#444"/></svg></span></div>
  <div class="col-rule" style="left:196px;top:638px;width:485px"></div>

  <div class="posts">
    <div class="post" style="top:18px"><div class="thumb" role="img" aria-label="Thumbnail of a chocolate cupcake with cream"></div><b>Pellentesque lore<br>m ligula.</b><br>Lorem ipsum dol<br>sit amet, consectetur adipiscin<br>elit. <a>Read more</a></div>
    <div class="col-rule" style="left:0;top:106px;width:159px"></div>
    <div class="post" style="top:122px"><div class="thumb" role="img" aria-label="Thumbnail of a chocolate cupcake with cream"></div><b>Lorem ipsum dolor<br>sit amet</b><br>Curabitur lacus elit,<br>tellus. Morbi eget dui et dui con<br>sequat aliq libero lectus bibend<br>um magna. <a>Read more</a></div>
    <div class="col-rule" style="left:0;top:226px;width:159px"></div>
    <div class="post" style="top:243px"><div class="thumb" role="img" aria-label="Thumbnail of a chocolate cupcake with cream"></div><b>Lorem ipsum dolor</b></div>
  </div>

  <article class="recipe" style="left:371px;top:658px">
    <div class="photo" role="img" aria-label="Photo of a plated dish with greens and sauce" style="background:linear-gradient(160deg,#c9a46a,#6f8a4a 50%,#d9cdb6)"></div>
    Pomegranate Chocolate Cup cakes with Buttercream Frosting<a>Read more</a>
  </article>
  <article class="recipe" style="left:534px;top:658px">
    <div class="photo" role="img" aria-label="Photo of stacked pancakes topped with coconut and a cherry" style="background:linear-gradient(160deg,#6ea070,#d08a3a 45%,#b8672a)"></div>
    Pomegranate Chocolate Cup cakes with Buttercream Frosting<a>Read more</a>
  </article>
  <div class="col-rule" style="left:364px;top:854px;width:317px"></div>
  <div role="img" aria-label="Photo of a pastry" style="position:absolute;left:371px;top:873px;width:148px;height:23px;background:linear-gradient(#c46a6a,#d9a07a)"></div>
  <p style="position:absolute;left:534px;top:872px;width:150px;font-size:12px;line-height:14.5px">These Coconut Buttermilk Pancakes with Orange Syrup</p>

  <h2 class="section-title" style="left:720px;top:493px">Renata Latest Video</h2>
  <div class="pager" style="left:945px;top:493px"><span><svg width="5" height="8"><path d="M5 0v8L0 4z" fill="#bbb"/></svg></span><span><svg width="5" height="8"><path d="M0 0v8l5-4z" fill="#444"/></svg></span></div>
  <div class="video"><svg width="14" height="17" viewBox="0 0 14 17"><path d="M0 0v17l14-8.5z" fill="#fff"/></svg></div>
  <p class="video-text">Here's a fun clip of what went on behind the scenes at<br>the photo shoot of Marquetta's new book: MARQUETTISSIMA!<small>See more at: <a>http://www.marquetta.example/#sthash.DyCbnF19.dpuf</a></small></p>
  <div class="side-rule"></div>
  <div class="tweets-title"><i></i><span>Renata Tweets</span></div>
  <p class="tweet"><a>@anonymous</a> Alter your weekend plans. Whatever<br>they are, they should start with these Coconut<br>Buttermilk Pancakes with Orange...<br><a>http://lnk.example/bnoXNDmu2s</a></p>
  <div class="tweet-rule"></div>
  <p class="tweet-next">This week we are sharing our new favourite breakfast</p>
</body>
</html>
```